E-commerce portal dedicated for selling books

We are looking for a design of a professional and official e-commerce web-site for a new company that is specialized in selling books (both books formats, printed and electronic), we’ll deal also with used-books where we plan to buy used books and re-sell them to other clients, or let the clients can sell their used-books directly to another client,
Web site must be very clear for users who like to brows the site contents or to buy a book, we will make the books available in discounted prices.
Customer should be able to perform the following actions in the site:
Search the book he/she is looking for easily
Get a brief description and details about the author, publisher, book content, browse the book’s content, browse first 20 pages ,
View similar or related books and a list of books that other users who bought this books also bought
Read and write reviews
Sign-up in the site
Complete the purchase process
Users can also sell or buy used-books from the site.
Look and feel:
The site’s look and feel is preferred to be clean, simple and balanced
Web site design is preferred to be simple with no strong or dark colors
User should feel comfort when looking at the home page because the design simplicity and comfortable colors
I liked the following sites’ look and feel:
http://www.qirtas.ae/
http://www.velmora.com/
http://www.tulvinghart.com/
Please be sure to include all common elements that are used in the e-commerce web sites like Search, online form(s), shopping cart / ordering, user log in/member, printer-friendly function, subscription to newsletter.....

```html
<!DOCTYPE html>
<html lang="en">
<head>
<meta charset="utf-8">
<title>Pagehaven – Books Online</title>
<link rel="stylesheet" href="https://fonts.googleapis.com/css2?family=Oswald:wght@300;400;500;700&family=Arimo:wght@400;700&display=swap">
<style>
:root{
  --blue:#1f66a5;
  --blue-dark:#124f85;
  --heading-blue:#1e6bab;
  --ink:#333333;
  --muted:#777777;
  --line:#dcdcdc;
  --red:#d71f1f;
  --gold:#f0b41c;
  --page:#f3f3f3;
  --footer:#5d5d5d;
  --btn-dark:#2e2e2e;
}
*{box-sizing:border-box;margin:0;padding:0}
html,body{width:758px;height:1200px;overflow:hidden}
body{position:relative;background:linear-gradient(#f9f9f9,#f0f0f0 40%,#f5f5f5);font-family:"Arimo",Arial,sans-serif;color:var(--ink)}
a{color:inherit;text-decoration:none}
.topbar{position:absolute;left:0;top:0;width:758px;height:6px;background:#6a6a6a}
.abs{position:absolute}

/* header */
.brand{left:83px;top:20px;font-family:"Oswald",sans-serif;font-weight:700;font-size:31px;letter-spacing:.5px;color:#2a6ea8;line-height:1}
.util-links{left:498px;top:26px;font-family:"Oswald",sans-serif;font-size:8.5px;color:var(--blue);display:flex;gap:0}
.util-links a{padding:0 5px;border-left:1px solid var(--blue);line-height:10px}
.util-links a:first-child{border-left:0;padding-left:0}
.signup{left:623px;top:21px;width:52px;height:17px;background:var(--blue);color:#fff;font-family:"Oswald",sans-serif;font-size:8.5px;text-align:center;line-height:17px}
.social{left:598px;top:54px;display:flex;gap:9px}
.social span{width:10px;height:10px;background:#2a6ea8;border-radius:2px}
.search{left:83px;top:74px;width:352px;height:28px;background:#fff;border:1px solid #e1e1e1}
.search-input{position:absolute;left:9px;top:9px;font-family:"Oswald",sans-serif;font-weight:300;font-size:7.5px;color:#aaa}
.search-cat{position:absolute;left:253px;top:4px;width:94px;height:19px;border:1px solid #d6d6d6;background:#f5f5f5;font-family:"Oswald",sans-serif;font-weight:300;font-size:7.5px;line-height:17px;padding-left:6px;color:#555}
.search-cat::after{content:"";position:absolute;right:0;top:0;width:18px;height:17px;border-left:1px solid #d6d6d6}
.search-cat svg{position:absolute;right:6px;top:7px}
.search-btn{left:434px;top:74px;width:58px;height:28px;background:var(--blue);color:#fff;font-family:"Oswald",sans-serif;font-size:13px;text-align:center;line-height:28px}
.account{left:500px;top:83px;display:flex;align-items:center;font-family:"Oswald",sans-serif;font-size:9px;color:var(--blue)}
.account span{display:flex;align-items:center;gap:3px;padding:0 9px;border-left:1px solid #9fb8cf;line-height:11px}
.account span:first-child{border-left:0;padding-left:0}
.caret{font-size:6px}

/* nav */
.mainnav{left:83px;top:114px;width:591px;height:26px;background:var(--blue)}
.mainnav a{position:absolute;top:0;height:26px;line-height:26px;font-family:"Oswald",sans-serif;font-weight:300;font-size:8.5px;color:#fff}
.mainnav .current{left:0;width:40px;background:var(--blue-dark);text-align:center}
.mainnav .current::after{content:"";position:absolute;left:16px;bottom:-4px;border:4px solid transparent;border-bottom:0;border-top-color:var(--blue-dark)}

/* hero */
.hero{left:83px;top:152px;width:591px;height:208px;background:#fff;box-shadow:0 1px 3px rgba(0,0,0,.15)}
.hero-cover{left:29px;top:22px;width:104px;height:166px;background:linear-gradient(100deg,#c9a400,#f4d21a 25%,#f6dc35 70%,#d7b80a)}
.hero-title{left:161px;top:30px;font-family:"Oswald",sans-serif;font-weight:700;font-size:22px;color:#1d5e97;line-height:1}
.hero-by{left:161px;top:61px;font-family:"Oswald",sans-serif;font-weight:300;font-size:8px;color:#555}
.hero-desc{left:161px;top:77px;width:212px;font-size:6.6px;line-height:8.3px;color:#555}
.hero-price{left:161px;top:125px;display:flex;align-items:center;gap:8px}
.hero-price s{font-family:"Oswald",sans-serif;font-size:12px;color:#999}
.hero-price b{font-family:"Oswald",sans-serif;font-size:20px;color:var(--red);font-weight:500}
.hero-stars{font-size:13px;color:var(--gold);letter-spacing:1px}
.hero-stars i{color:#ccc;font-style:normal}
.btn{display:inline-block;color:#fff;font-family:"Arimo",sans-serif;font-weight:700;text-align:center}
.hero-browse{left:161px;top:154px;width:50px;height:21px;line-height:21px;font-size:9.5px;background:var(--btn-dark)}
.hero-cart{left:219px;top:154px;width:73px;height:21px;line-height:21px;font-size:9.5px;background:var(--blue)}
.hero-side{left:393px;top:4px;width:198px;height:200px;background:#d6d6d6}
.hero-collage{left:22px;top:18px;width:150px;height:126px;background:linear-gradient(90deg,#1d3f78 0,#23527e 30%,#2f3b3c 45%,#3a4c56 70%,#4aa8de 85%,#5db7e4)}
.view-more{left:57px;top:156px;width:68px;height:21px;line-height:21px;font-size:9.5px;background:var(--blue)}
.hero-from{left:0;top:186px;width:198px;text-align:center;font-size:7.5px;font-weight:700;color:#555}
.hero-dots{left:322px;top:368px;display:flex;align-items:center;gap:6px}
.hero-dots span{width:9px;height:9px;border-radius:50%;border:1.5px solid #c8c8c8}
.hero-dots .on{background:var(--blue);border-color:var(--blue)}

/* sidebar */
.topics{left:83px;top:389px;width:110px}
.side-title,.section-title{font-family:"Oswald",sans-serif;font-size:13.5px;color:var(--heading-blue);font-weight:400;line-height:1}
.topic-list{list-style:none;margin-top:10px}
.topic-list li{font-size:6.7px;line-height:12.05px;color:#666}
.side-rule{left:197px;top:395px;width:1px;height:620px;background:linear-gradient(#e2e2e2,#e2e2e2 85%,rgba(226,226,226,0))}

/* shelves */
.shelf{left:216px;width:461px;height:210px}
.section-title{position:absolute;left:0;top:0}
.shelf-rule{position:absolute;left:0;top:17px;width:461px;height:1px;background:var(--line)}
.book-row{position:absolute;left:0;top:30px;width:480px;display:flex;gap:0}
.book-card{width:120px;position:relative;height:170px}
.book-cover{width:64px;height:95px}
.cover-clear{background:linear-gradient(160deg,#a9482f 0,#c55f3a 25%,#7f8d9b 60%,#2d3c4e)}
.cover-mini{background:linear-gradient(160deg,#7fd2c7,#3cb0ad 40%,#6ec8c0 70%,#2b8aa0)}
.cover-night{background:linear-gradient(170deg,#a44a18,#c76a22 40%,#8d3b12 80%,#5a2408)}
.cover-mercy{background:linear-gradient(165deg,#2b4466,#3c5e86 40%,#2e4a6c 75%,#1f3550)}
.book-title{margin-top:9px;font-size:6.8px;line-height:8.3px;font-weight:700;color:var(--blue);width:100px}
.book-author{font-size:6.5px;color:#666;margin-top:2px}
.rating{font-size:8px;color:var(--gold);letter-spacing:.6px;margin-top:1px;line-height:10px}
.rating i{font-style:normal;color:#ccc}
.price{display:flex;align-items:baseline;gap:10px;margin-top:1px}
.price s{font-size:6.5px;color:#888}
.price b{font-size:9.5px;color:var(--red);font-weight:400}
.card-actions{display:flex;gap:3px;margin-top:2px}
.card-actions a{height:12px;line-height:12px;font-size:7.2px;font-weight:700;color:#fff;padding:0 3px}
.btn-details{background:var(--btn-dark)}
.btn-cart{background:var(--blue)}
.arrow-prev{position:absolute;left:-11px;top:38px}
.arrow-next{position:absolute;left:460px;top:38px}

/* promos */
.promo{left:83px;top:1076px;width:289px;height:64px;background:linear-gradient(100deg,#8b8f86,#c9c7b8 40%,#7d7f76 70%,#d9d6c8);overflow:hidden}
.promo-photo{position:absolute;inset:0}
.promo-red{position:absolute;left:0;top:0;width:180px;height:64px;background:var(--red);clip-path:polygon(0 0,148px 0,180px 64px,0 64px)}
.promo-big{position:absolute;left:10px;top:6px;font-family:"Arimo",sans-serif;font-size:16px;color:#fff;line-height:1}
.promo-small{position:absolute;left:11px;top:25px;font-size:9px;color:#fff}
.promo-brand{position:absolute;left:11px;top:38px;font-family:"Oswald",sans-serif;font-weight:700;font-size:18px;color:#fff;line-height:1}
.newsletter{left:386px;top:1076px;width:289px;height:64px;background:var(--blue)}
.newsletter h2{position:absolute;left:8px;top:9px;font-family:"Oswald",sans-serif;font-weight:400;font-size:11.5px;color:#fff}
.news-input{position:absolute;left:7px;top:32px;width:218px;height:26px;background:#fff;font-family:"Oswald",sans-serif;font-weight:300;font-size:7.5px;color:#aaa;line-height:26px;padding-left:7px}
.news-submit{position:absolute;left:225px;top:32px;width:56px;height:26px;background:var(--btn-dark);color:#fff;font-family:"Oswald",sans-serif;font-size:12px;text-align:center;line-height:26px}

/* footer */
.site-footer{left:0;top:1161px;width:758px;height:39px;background:var(--footer);color:#fff;font-size:6.8px}
.site-footer .legal{position:absolute;left:84px;top:14px}
.site-footer .copy{position:absolute;right:84px;top:14px}
</style>
</head>
<body>
<div class="topbar"></div>

<header>
  <div class="abs brand">PAGEHAVEN</div>
  <nav class="abs util-links"><a href="#">HELP</a><a href="#">FORUMS</a><a href="#">COMMUNITY</a></nav>
  <a class="abs signup" href="#">SIGN UP</a>
  <div class="abs social" aria-label="Social links"><span></span><span></span><span></span><span></span></div>

  <form class="abs search">
    <span class="search-input">ENTER BOOKS, AUTHORS, OR PUBLISHER</span>
    <span class="search-cat">ALL CATEGORIES
      <svg width="6" height="4" viewBox="0 0 6 4"><path d="M0 0h6L3 4z" fill="#777"/></svg>
    </span>
  </form>
  <a class="abs search-btn" href="#">SEARCH</a>

  <div class="abs account">
    <span>SIGN IN <b class="caret">▼</b></span>
    <span>
      <svg width="13" height="10" viewBox="0 0 13 10"><path d="M0 1h2.5l2 6h6.5l1.5-4.5H4" fill="none" stroke="#1f66a5" stroke-width="1.1"/><circle cx="5.5" cy="9" r="0.9" fill="#1f66a5"/><circle cx="10" cy="9" r="0.9" fill="#1f66a5"/></svg>
      CART <b class="caret">▼</b></span>
    <span>WISH LIST <b class="caret">▼</b></span>
  </div>

  <nav class="abs mainnav">
    <a class="current" href="#">HOME</a>
    <a style="left:59px" href="#">ALL BOOKS</a>
    <a style="left:129px" href="#">ON SALE</a>
    <a style="left:189px" href="#">SELL BOOKS</a>
    <a style="left:262px" href="#">REVIEWS</a>
    <a style="left:318px" href="#">DEALS &amp; OFFERS</a>
    <a style="left:407px" href="#">ABOUT US</a>
    <a style="left:475px" href="#">CONTACT US</a>
  </nav>
</header>

<section class="abs hero">
  <div class="abs hero-cover" role="img" aria-label="Yellow front cover of the featured novel Voltreach"></div>
  <h1 class="abs hero-title">VOLTREACH</h1>
  <p class="abs hero-by">BY LORNE ABERNATHY (1984)</p>
  <p class="abs hero-desc">This was a virtually impossible task. Put together a list of 50 must-read science fiction books and don't make anyone angry. Science fiction is the most discussed and argued over genre in literature but it actually goes way beyond books and into film, TV, video games and even toys.</p>
  <div class="abs hero-price"><s>$30</s><b>$24</b><span class="hero-stars">★★★★<i>☆</i></span></div>
  <a class="abs btn hero-browse" href="#">Browse</a>
  <a class="abs btn hero-cart" href="#">Add to Cart</a>
  <aside class="abs hero-side">
    <div class="abs hero-collage" role="img" aria-label="Stack of other book covers by Lorne Abernathy"></div>
    <a class="abs btn view-more" href="#">View More</a>
    <p class="abs hero-from">from Lorne Abernathy</p>
  </aside>
</section>
<div class="abs hero-dots">
  <svg width="8" height="8" viewBox="0 0 8 8"><path d="M7 0v8L0 4z" fill="#c8c8c8"/></svg>
  <span class="on"></span><span></span><span></span><span></span><span></span>
  <svg width="8" height="8" viewBox="0 0 8 8"><path d="M1 0v8l7-4z" fill="#c8c8c8"/></svg>
</div>

<aside class="abs topics">
  <h2 class="side-title">TOPICS</h2>
  <ul class="topic-list">
    <li>Antiques &amp; Collectibles</li><li>Architecture</li><li>Art</li><li>Biographies &amp; Autobiographies</li><li>Body, Mind &amp; Spirit</li><li>Business &amp; Economics</li><li>Children's Fiction</li><li>Children's Non-Fiction</li><li>Comics &amp; Graphic Novels</li><li>Computers &amp; the Internet</li><li>Cooking</li><li>Crafts &amp; Hobbies</li><li>Drama</li><li>Education</li><li>Family &amp; Relationships</li><li>Fiction</li><li>Games</li><li>Gardening</li><li>Geography</li><li>Health &amp; Fitness</li><li>History</li><li>House &amp; Home</li><li>Humor</li><li>Language Arts &amp; Disciplines</li><li>Language Study</li><li>Law</li><li>Literary Collections</li><li>Literary Criticism</li><li>Mathematics</li><li>Medical</li><li>Music</li><li>Nature</li><li>Performing Arts</li><li>Pets</li><li>Philosophy</li><li>Photography</li><li>Poetry</li><li>Political Science</li><li>Psychology &amp; Psychiatry</li><li>Reference</li><li>Religion</li><li>Science</li><li>Self-Help</li><li>Social Sciences</li><li>Sports &amp; Recreation</li><li>Study Aids</li><li>Technology</li><li>Transportation</li><li>Travel</li><li>True Crime</li>
  </ul>
</aside>
<div class="abs side-rule"></div>

<!-- POPULAR -->
<section class="abs shelf" style="top:390px">
  <h2 class="section-title">POPULAR</h2><div class="shelf-rule"></div>
  <div class="book-row">
    <article class="book-card"><div class="book-cover cover-clear" role="img" aria-label="Cover of Clear Path with author portrait"></div><h3 class="book-title">Clear Path: The New Rules for Thriving in the Modern World</h3><p class="book-author">Dale Hensworth</p><div class="rating">★★★★<i>☆</i></div><p class="price"><s>$26.00</s><b>$20.00</b></p><div class="card-actions"><a class="btn-details" href="#">Details</a><a class="btn-cart" href="#">Add to Cart</a></div></article>
    <article class="book-card"><div class="book-cover cover-mini" role="img" aria-label="Cover of Minibakes with cake pops"></div><h3 class="book-title">160 Best Minibakes Cake Pop Maker Recipes</h3><p class="book-author">Nora Pell &amp; Tessa Quill</p><div class="rating">★★★★<i>☆</i></div><p class="price"><s>$24.95</s><b>$13.85</b></p><div class="card-actions"><a class="btn-details" href="#">Details</a><a class="btn-cart" href="#">Add to Cart</a></div></article>
    <article class="book-card"><div class="book-cover cover-night" role="img" aria-label="Cover of Long Night R in rusted orange tones"></div><h3 class="book-title">Long Night R: An Oral History of the Undead War</h3><p class="book-author">Owen Strand</p><div class="rating">★★★★<i>☆</i></div><p class="price"><s>$14.95</s><b>$8.27</b></p><div class="card-actions"><a class="btn-details" href="#">Details</a><a class="btn-cart" href="#">Add to Cart</a></div></article>
    <article class="book-card"><div class="book-cover cover-mercy" role="img" aria-label="Cover of Mercy Goes Unanswered in navy tones"></div><h3 class="book-title">Mercy Goes Unanswered</h3><p class="book-author">Wade Harlan</p><div class="rating">★★★★<i>☆</i></div><p class="price"><s>$14.00</s><b>$9.02</b></p><div class="card-actions"><a class="btn-details" href="#">Details</a><a class="btn-cart" href="#">Add to Cart</a></div></article>
  </div>
  <svg class="arrow-prev" width="7" height="44" viewBox="0 0 7 44"><path d="M7 0C2 10 0 16 0 22s2 12 7 22z" fill="#e3e3e3"/></svg>
  <svg class="arrow-next" width="7" height="44" viewBox="0 0 7 44"><path d="M0 0l7 22-7 22C3 32 3 12 0 0z" fill="#1f66a5"/></svg>
</section>

<!-- LATEST -->
<section class="abs shelf" style="top:618px">
  <h2 class="section-title">LATEST</h2><div class="shelf-rule"></div>
  <div class="book-row">
    <article class="book-card"><div class="book-cover cover-mini" role="img" aria-label="Cover of Minibakes with cake pops"></div><h3 class="book-title">160 Best Minibakes Cake Pop Maker Recipes</h3><p class="book-author">Nora Pell &amp; Tessa Quill</p><div class="rating">★★★★<i>☆</i></div><p class="price"><s>$24.95</s><b>$13.85</b></p><div class="card-actions"><a class="btn-details" href="#">Details</a><a class="btn-cart" href="#">Add to Cart</a></div></article>
    <article class="book-card"><div class="book-cover cover-mercy" role="img" aria-label="Cover of Mercy Goes Unanswered in navy tones"></div><h3 class="book-title">Mercy Goes Unanswered</h3><p class="book-author">Wade Harlan</p><div class="rating">★★★★<i>☆</i></div><p class="price"><s>$14.00</s><b>$9.02</b></p><div class="card-actions"><a class="btn-details" href="#">Details</a><a class="btn-cart" href="#">Add to Cart</a></div></article>
    <article class="book-card"><div class="book-cover cover-night" role="img" aria-label="Cover of Long Night R in rusted orange tones"></div><h3 class="book-title">Long Night R: An Oral History of the Undead War</h3><p class="book-author">Owen Strand</p><div class="rating">★★★★<i>☆</i></div><p class="price"><s>$14.95</s><b>$8.27</b></p><div class="card-actions"><a class="btn-details" href="#">Details</a><a class="btn-cart" href="#">Add to Cart</a></div></article>
    <article class="book-card"><div class="book-cover cover-clear" role="img" aria-label="Cover of Clear Path with author portrait"></div><h3 class="book-title">Clear Path: The New Rules for Thriving in the Modern World</h3><p class="book-author">Dale Hensworth</p><div class="rating">★★★★<i>☆</i></div><p class="price"><s>$26.00</s><b>$20.00</b></p><div class="card-actions"><a class="btn-details" href="#">Details</a><a class="btn-cart" href="#">Add to Cart</a></div></article>
  </div>
  <svg class="arrow-prev" width="7" height="44" viewBox="0 0 7 44"><path d="M7 0C2 10 0 16 0 22s2 12 7 22z" fill="#e3e3e3"/></svg>
  <svg class="arrow-next" width="7" height="44" viewBox="0 0 7 44"><path d="M0 0l7 22-7 22C3 32 3 12 0 0z" fill="#1f66a5"/></svg>
</section>

<!-- RECOMMENDED -->
<section class="abs shelf" style="top:847px">
  <h2 class="section-title">RECOMMENDED FOR YOU</h2><div class="shelf-rule"></div>
  <div class="book-row">
    <article class="book-card"><div class="book-cover cover-clear" role="img" aria-label="Cover of Clear Path with author portrait"></div><h3 class="book-title">Clear Path: The New Rules for Thriving in the Modern World</h3><p class="book-author">Dale Hensworth</p><div class="rating">★★★★<i>☆</i></div><p class="price"><s>$26.00</s><b>$20.00</b></p><div class="card-actions"><a class="btn-details" href="#">Details</a><a class="btn-cart" href="#">Add to Cart</a></div></article>
    <article class="book-card"><div class="book-cover cover-mini" role="img" aria-label="Cover of Minibakes with cake pops"></div><h3 class="book-title">160 Best Minibakes Cake Pop Maker Recipes</h3><p class="book-author">Nora Pell &amp; Tessa Quill</p><div class="rating">★★★★<i>☆</i></div><p class="price"><s>$24.95</s><b>$13.85</b></p><div class="card-actions"><a class="btn-details" href="#">Details</a><a class="btn-cart" href="#">Add to Cart</a></div></article>
    <article class="book-card"><div class="book-cover cover-night" role="img" aria-label="Cover of Long Night R in rusted orange tones"></div><h3 class="book-title">Long Night R: An Oral History of the Undead War</h3><p class="book-author">Owen Strand</p><div class="rating">★★★★<i>☆</i></div><p class="price"><s>$14.95</s><b>$8.27</b></p><div class="card-actions"><a class="btn-details" href="#">Details</a><a class="btn-cart" href="#">Add to Cart</a></div></article>
    <article class="book-card"><div class="book-cover cover-mercy" role="img" aria-label="Cover of Mercy Goes Unanswered in navy tones"></div><h3 class="book-title">Mercy Goes Unanswered</h3><p class="book-author">Wade Harlan</p><div class="rating">★★★★<i>☆</i></div><p class="price"><s>$14.00</s><b>$9.02</b></p><div class="card-actions"><a class="btn-details" href="#">Details</a><a class="btn-cart" href="#">Add to Cart</a></div></article>
  </div>
  <svg class="arrow-prev" width="7" height="44" viewBox="0 0 7 44"><path d="M7 0C2 10 0 16 0 22s2 12 7 22z" fill="#e3e3e3"/></svg>
  <svg class="arrow-next" width="7" height="44" viewBox="0 0 7 44"><path d="M0 0l7 22-7 22C3 32 3 12 0 0z" fill="#1f66a5"/></svg>
</section>

<aside class="abs promo">
  <div class="promo-photo" role="img" aria-label="Close-up of pencils resting on open book pages"></div>
  <div class="promo-red"></div>
  <p class="promo-big">Save upto 40%</p>
  <p class="promo-small">on the best deals of</p>
  <p class="promo-brand">PAGEHAVEN</p>
</aside>

<form class="abs newsletter">
  <h2>SUBSCRIBE TO THE NEWSLETTER</h2>
  <span class="news-input">ENTER YOUR EMAIL ADRESS HERE</span>
  <span class="news-submit">SUBMIT</span>
</form>

<footer class="abs site-footer">
  <span class="legal">Terms of Use, Copyright, and Privacy Policy</span>
  <span class="copy">© 2013 Pagehaven.com</span>
</footer>
</body>
</html>
```